Brochure design for healthcare software company

We need a tri-fold brochure design for our healthcare software company that provides software and services for clinicians who manage patients who have or may be diagnosed with cancer.

We have an existing web, business card design and trade show booth design and want the ultimate design to be consistent with these. All of the files including stock images are provided.

Target Market(s)

Nurses, Healthcare professionals

Industry/Entity Type

Healthcare

Requirements
Must have
• Design consistent with attached tradeshow booth and business card.

```html
<!DOCTYPE html>
<html lang="en">
<head>
<meta charset="utf-8">
<title>Veloracare Navigation – Tri-fold Brochure</title>
<link rel="stylesheet" href="https://fonts.googleapis.com/css2?family=Didact+Gothic&display=swap">
<style>
  :root {
    --page-bg: #e4e5e7;
    --paper: #ffffff;
    --ink: #2b2d33;
    --ink-soft: #5b5e66;
    --brand-blue: #1f4fb8;
    --deep-blue: #0b2a78;
    --night-blue: #071a4f;
    --glow-blue: #36a6f0;
    --brand-green: #23b266;
    --green-dark: #149a52;
  }
  * { box-sizing: border-box; margin: 0; padding: 0; }
  html, body {
    width: 1200px; height: 900px; overflow: hidden;
    background: var(--page-bg);
    font-family: "Didact Gothic", "Century Gothic", sans-serif;
    color: var(--ink);
  }
  .brochure {
    position: absolute; left: 60px; top: 50px;
    width: 1080px; height: 800px;
    display: flex;
    box-shadow: 0 18px 40px rgba(0,0,0,.18);
  }
  .panel { position: relative; width: 360px; height: 100%; overflow: hidden; }
  .panel + .panel { border-left: 1px solid rgba(0,0,0,.08); }

  .heading {
    font-size: 22px; font-weight: 400; letter-spacing: .5px;
    text-decoration: underline; text-underline-offset: 5px;
    text-decoration-thickness: 1.5px;
  }
  .copy { font-size: 13px; line-height: 1.6; letter-spacing: .3px; }
  .green-band { position: absolute; left: 0; right: 0; bottom: 0; height: 40px; background: var(--brand-green); }

  /* Cover panel */
  .panel--cover { background: var(--paper); padding: 60px 40px 0; text-align: center; }
  .brand { display: flex; align-items: center; justify-content: center; gap: 10px; }
  .brand__mark { width: 22px; height: 22px; border-radius: 50%; background: var(--brand-blue); }
  .brand__name { font-size: 16px; letter-spacing: 5px; color: var(--brand-blue); }
  .panel--cover .heading { margin-top: 40px; color: var(--ink); }
  .chart-visual {
    margin: 34px auto 0; width: 270px; height: 200px; border-radius: 10px;
    background: radial-gradient(ellipse at 55% 45%, #cfe3fb 0%, #a9cdf3 35%, #eef4fb 75%, #ffffff 100%);
  }
  .panel--cover .copy { margin-top: 60px; text-align: left; color: var(--ink-soft); }

  /* Inside panel */
  .panel--inside { color: #fff; padding: 70px 36px 0; }
  .inside-photo {
    position: absolute; inset: 0;
    background: linear-gradient(165deg, #3a6ad0 0%, var(--brand-blue) 30%, var(--deep-blue) 70%, var(--night-blue) 100%);
  }
  .inside-content { position: relative; }
  .panel--inside .heading { color: #fff; margin-top: 200px; }
  .panel--inside .heading + .copy { margin-top: 16px; }
  .panel--inside .copy + .heading { margin-top: 50px; }
  .panel--inside .copy { color: #dce6ff; }

  /* Flap panel */
  .panel--flap { background: var(--paper); display: flex; flex-direction: column; }
  .flap-top { padding: 50px 40px 30px; text-align: center; height: 220px; }
  .flap-top .heading { color: var(--ink); }
  .flap-top .copy { margin-top: 16px; font-size: 12px; color: var(--ink-soft); }
  .lock-visual {
    height: 290px;
    background: radial-gradient(circle at 50% 50%, var(--glow-blue) 0%, #1a5fc8 25%, var(--deep-blue) 60%, var(--night-blue) 100%);
  }
  .flap-bottom {
    flex: 1; background: var(--brand-green); color: #fff;
    padding: 40px 40px 0; text-align: center;
  }
  .flap-bottom .heading { color: #fff; }
  .flap-bottom .copy { margin-top: 16px; font-size: 12px; color: #eafff2; }
</style>
</head>
<body>
  <main class="brochure">
    <section class="panel panel--cover">
      <div class="brand">
        <span class="brand__mark"></span>
        <span class="brand__name">VELORACARE</span>
      </div>
      <h1 class="heading">Simplified navigation</h1>
      <div class="chart-visual" role="img" aria-label="Tablet showing blue analytics charts and graphs"></div>
      <p class="copy">Track all of your patients from their entry point, for example an abnormal screening exam or a positive diagnosis, through survivorship. Veloracare Navigation allows you to easily maintain a record of all referrals, exams, treatments, contacts, appointments and notes for your patients.</p>
      <div class="green-band"></div>
    </section>

    <section class="panel panel--inside">
      <div class="inside-photo" role="img" aria-label="Blue-toned photo of a clinical workspace"></div>
      <div class="inside-content">
        <h2 class="heading">Advantages</h2>
        <p class="copy">View and manage every patient in a single, completely customizable dashboard. Create workflows tailored to your care and navigation teams.</p>
        <h2 class="heading">Reports</h2>
        <p class="copy">Quickly generate navigation reports that show trends for your staff, including case loads, timelines, referrals and outcomes.</p>
      </div>
      <div class="green-band"></div>
    </section>

    <section class="panel panel--flap">
      <div class="flap-top">
        <h2 class="heading">Secure</h2>
        <p class="copy">Built from the ground up with security in mind, Veloracare Navigation is completely HIPAA compliant. Rest assured that your and your patients’ data is protected.</p>
      </div>
      <div class="lock-visual" role="img" aria-label="Glowing digital padlock on a blue circuit background"></div>
      <div class="flap-bottom">
        <h2 class="heading">Affordable</h2>
        <p class="copy">Veloracare Navigation is completely free for an unlimited number of users and facilities. Additional services including deployments, training, secure hosting and workflow consultations are available.</p>
      </div>
    </section>
  </main>
</body>
</html>
```